Medical Aesthetics business cards

Looking for a business card for my new medical aesthetics business. I am a nurse practitioner and will be administering dravine , fillers as well as providing other services

```html
<!DOCTYPE html>
<html lang="en">
<head>
<meta charset="utf-8">
<title>Dravine Aesthetics Business Card</title>
<link rel="stylesheet" href="https://fonts.googleapis.com/css2?family=Tinos:wght@400;700&display=swap">
<style>
  :root {
    --backdrop: #ecedef;
    --paper: #f4f4f2;
    --ink: #111111;
    --band: #262626;
    --band-line: #9a9a9a;
    --light-text: #f2f2f2;
    --address-text: #333333;
    --ornament: #8c8c8c;
  }
  * { margin: 0; padding: 0; box-sizing: border-box; }
  html, body {
    width: 1200px;
    height: 857px;
    overflow: hidden;
    background: var(--backdrop);
    font-family: "Tinos", "Times New Roman", serif;
  }
  .card {
    position: absolute;
    left: 100px;
    top: 142px;
    width: 1000px;
    height: 572px;
    background: var(--paper);
    box-shadow: 0 6px 18px rgba(0,0,0,0.12);
    overflow: hidden;
  }
  .card-frame {
    position: absolute;
    inset: 22px;
    border: 2px solid var(--ink);
  }
  .dark-band {
    position: absolute;
    left: 0;
    top: 322px;
    width: 960px;
    bottom: 0;
    background: var(--band);
  }
  .dark-band-frame {
    position: absolute;
    left: 20px;
    right: 0;
    top: 0;
    bottom: 20px;
    border-left: 1.5px solid var(--band-line);
    border-bottom: 1.5px solid var(--band-line);
  }
  .identity {
    position: absolute;
    left: 0;
    width: 960px;
    top: 150px;
    text-align: center;
  }
  .holder-name {
    font-size: 40px;
    font-weight: 400;
    letter-spacing: 1px;
    color: var(--ink);
    line-height: 1;
  }
  .holder-title {
    display: inline-block;
    margin-top: 10px;
    background: var(--ink);
    color: var(--light-text);
    font-size: 24px;
    line-height: 1.2;
    letter-spacing: 1px;
    padding: 4px 40px 3px;
    min-width: 430px;
  }
  .practice-address {
    margin-top: 10px;
    font-size: 23px;
    line-height: 1.2;
    color: var(--address-text);
    letter-spacing: 0.5px;
  }
  .ornament {
    position: absolute;
    left: 440px;
    top: 284px;
    width: 76px;
    height: 76px;
    border-radius: 50%;
    background: radial-gradient(circle, #d8d8d8 0%, var(--ornament) 70%, #555 100%);
  }
  .contact {
    position: absolute;
    left: 0;
    width: 960px;
    top: 378px;
    text-align: center;
    color: var(--light-text);
    font-size: 25px;
    line-height: 1.3;
  }
  .contact .phones span + span { margin-left: 18px; }
</style>
</head>
<body>
  <main class="card">
    <div class="card-frame"></div>
    <div class="dark-band"><div class="dark-band-frame"></div></div>
    <section class="identity">
      <h1 class="holder-name">YOUR NAME HERE</h1>
      <div class="holder-title">NURSE PRACTITIONER</div>
      <p class="practice-address">GALLERY NINE. 48 LINDEN ROW LARKFORD PA</p>
    </section>
    <div class="ornament" role="img" aria-label="Round geometric mandala ornament in grey tones"></div>
    <section class="contact">
      <p class="email">your Email Address Goes here</p>
      <p class="phones"><span>1.800.264.7130</span><span>610.482.3957</span></p>
    </section>
  </main>
</body>
</html>
```